Varden Ridge Concrete Pumping needs a logo design and is in the concrete industry

A creative design for this Varden Ridge Concrete Pumping business. Using a trailer mounted line pump, not a boom pump.
Colour to be used is orange and a mix of white or black writing.
Target Market(s)
General Public, anyone
Industry/Entity Type
Concrete
Contact Information for Business Card
Varden Ridge Concrete Pumping
Brennan Holloway
PO BOX 47
Merrin Vale VIC 3251
Phone: 0491552083
Email: Holloway@postwren.com.au
Colors
f37122
000000
ffffff
Requirements
Must have
- Details listed
Nice to have
- A great logo
Should not have
- anything silly

```html
<!DOCTYPE html>
<html lang="en">
<head>
<meta charset="UTF-8">
<title>Varden Ridge Concrete Pumping – Business Card</title>
<link rel="stylesheet" href="https://fonts.googleapis.com/css2?family=Open+Sans:wght@600;800&display=swap">
<style>
  :root {
    --backdrop: #a4a3a8;
    --card-black: #0c0c0d;
    --card-black-edge: #3a3a3c;
    --card-white: #f4f5f5;
    --brand-orange: #f37122;
    --brand-orange-light: #f79a5e;
    --text-dark: #1b1b1b;
    --shadow: rgba(0, 0, 0, 0.35);
  }
  * { margin: 0; padding: 0; box-sizing: border-box; }
  html, body {
    width: 1200px;
    height: 863px;
    overflow: hidden;
    background: var(--backdrop);
    font-family: "Open Sans", Arial, sans-serif;
  }
  .card-set {
    position: absolute;
    inset: 0;
    display: flex;
    align-items: center;
    justify-content: center;
    gap: 50px;
  }
  .card {
    position: relative;
    width: 520px;
    height: 318px;
    overflow: hidden;
    box-shadow: 0 14px 30px var(--shadow);
  }
  .card-front {
    background: linear-gradient(135deg, var(--card-black) 0%, var(--card-black) 45%, var(--card-black-edge) 100%);
  }
  .card-back { background: var(--card-white); }
  .card-back .swoosh {
    position: absolute;
    inset: 0;
    width: 100%;
    height: 100%;
  }
  .wordmark {
    position: absolute;
    display: flex;
    align-items: center;
    gap: 10px;
    color: var(--brand-orange);
    font-weight: 800;
    line-height: 1.05;
    white-space: nowrap;
  }
  .wordmark .mark-dot {
    flex: none;
    width: 22px;
    height: 22px;
    border-radius: 50%;
    background: var(--brand-orange);
  }
  .card-front .wordmark {
    left: 50%;
    top: 50%;
    transform: translate(-50%, -50%);
    font-size: 30px;
  }
  .card-back .wordmark {
    right: 30px;
    top: 84px;
    font-size: 24px;
    color: var(--text-dark);
  }
  .card-back .wordmark .mark-dot { background: var(--text-dark); }
  .contact {
    position: absolute;
    left: 34px;
    top: 156px;
    list-style: none;
    color: var(--text-dark);
    font-weight: 600;
    font-size: 12.5px;
    line-height: 1.55;
  }
  .contact .contact-name { font-weight: 800; font-size: 14px; }
  .contact .address { margin-bottom: 8px; }
</style>
</head>
<body>
  <main class="card-set">
    <section class="card card-front" aria-label="Business card front">
      <div class="wordmark">
        <span class="mark-dot"></span>
        <span class="wordmark-name">Varden Ridge<br>Concrete Pumping</span>
      </div>
    </section>

    <section class="card card-back" aria-label="Business card back">
      <svg class="swoosh" viewBox="0 0 520 318" preserveAspectRatio="none" aria-hidden="true">
        <path d="M0 0 H300 C180 20 70 90 0 170 Z" fill="var(--brand-orange)"/>
        <path d="M520 80 V318 H250 C370 300 470 220 520 80 Z" fill="var(--brand-orange-light)"/>
      </svg>
      <div class="wordmark">
        <span class="mark-dot"></span>
        <span class="wordmark-name">Varden Ridge<br>Concrete Pumping</span>
      </div>
      <ul class="contact">
        <li class="contact-name">Brennan Holloway</li>
        <li class="address">PO BOX 47, Merrin Vale VIC 3251</li>
        <li>P: 0491552083</li>
        <li>E: Holloway@postwren.com.au</li>
      </ul>
    </section>
  </main>
</body>
</html>
```